Business card design

We need a business card design for our law firm in Australia. Our firm's name is "KD LORN Lawyers & Notary". Our slogan is "Every Matter Handled with Steady Care".

We would like to use the burgundy tone.

Industry/Entity Type

Law Firm

Contact Information for Business Card

Clara Bexley
Solicitor
Notary Public (Qld & Vic)
Migration Agent
LLB, LLM, Grad Dip in LP, Grad Dip in NP
RMA 0853162

Office Address: 24/6 Tolvern Road Marleigh QLD 4287 Australia
Postal Address: P O Box 61 Marleigh QLD 4287 Australia
Telephone: 1300 274 563
Facsimile: 1300 274 569
International Telephone: +617 3956 2740
International Facsimile: +617 3871 6025
Email: clara.bexley@kdlornlegal.example
Web: www.kdlornlegal.example

```html
<!DOCTYPE html>
<html lang="en">
<head>
<meta charset="utf-8">
<title>KD LORN Lawyers &amp; Notary – Business Card</title>
<link rel="stylesheet" href="https://fonts.googleapis.com/css2?family=Cinzel:wght@400;700&family=Tinos:ital@0;1&display=swap">
<style>
  :root {
    --backdrop: #2e1212;
    --card-white: #ffffff;
    --card-shade: #dedede;
    --burgundy: #b3070c;
    --burgundy-deep: #8e0307;
    --burgundy-bright: #cc0a10;
    --rule-light: rgba(255, 255, 255, 0.55);
    --ink: #3a3a3a;
    --ink-soft: #5a5a5a;
    --name-ink: #ffffff;
  }

  * { margin: 0; padding: 0; box-sizing: border-box; }

  html, body {
    width: 1200px;
    height: 990px;
    overflow: hidden;
    background: var(--backdrop);
  }

  .canvas { position: relative; width: 1200px; height: 990px; }

  .business-card {
    position: absolute;
    left: 60px;
    top: 188px;
    width: 1080px;
    height: 614px;
    background: radial-gradient(ellipse 60% 70% at 50% 50%, var(--card-white) 0%, #f7f7f7 45%, var(--card-shade) 100%);
    box-shadow: 0 10px 30px rgba(0, 0, 0, 0.45);
    overflow: hidden;
  }

  .firm-name {
    position: absolute;
    left: 0;
    right: 0;
    top: 26px;
    text-align: center;
    font-family: "Cinzel", serif;
    font-weight: 400;
    color: var(--burgundy);
    line-height: 1;
  }
  .firm-name__main {
    display: block;
    font-size: 112px;
    letter-spacing: 2px;
  }
  .firm-name__sub {
    display: block;
    margin-top: 10px;
    font-size: 38px;
    letter-spacing: 6px;
  }

  .rule-thin {
    position: absolute;
    left: 0;
    width: 100%;
    height: 7px;
    background: var(--burgundy-bright);
  }
  .rule-thin--upper { top: 220px; }
  .rule-thin--lower { top: 387px; height: 8px; }

  .name-band {
    position: absolute;
    left: 0;
    top: 236px;
    width: 100%;
    height: 141px;
    background: linear-gradient(180deg, var(--burgundy-deep) 0%, var(--burgundy-bright) 40%, var(--burgundy) 100%);
    color: var(--name-ink);
    text-align: center;
  }

  .holder-name {
    position: absolute;
    left: 0;
    right: 0;
    top: 16px;
    font-family: "Cinzel", serif;
    font-weight: 700;
    font-size: 40px;
    line-height: 1;
    letter-spacing: 1px;
  }

  .name-divider {
    position: absolute;
    left: 50%;
    top: 64px;
    width: 447px;
    height: 1px;
    margin-left: -223px;
    background: var(--rule-light);
  }

  .holder-credentials {
    position: absolute;
    left: 0;
    right: 0;
    top: 76px;
    font-family: "Cinzel", serif;
    font-weight: 400;
    font-size: 18px;
    line-height: 27px;
    letter-spacing: 0.5px;
  }

  .slogan {
    position: absolute;
    left: 0;
    right: 0;
    top: 410px;
    text-align: center;
    font-family: "Tinos", serif;
    font-style: italic;
    font-size: 24px;
    line-height: 1;
    color: var(--burgundy);
  }

  .contact-details {
    position: absolute;
    left: 70px;
    right: 70px;
    top: 456px;
    display: flex;
    justify-content: space-between;
    font-family: "Tinos", serif;
    font-size: 20px;
    line-height: 34px;
    color: var(--ink);
  }

  .contact-column { list-style: none; }
  .contact-label { color: var(--ink-soft); }
</style>
</head>
<body>
  <main class="canvas">
    <section class="business-card" aria-label="Business card for Clara Bexley, KD LORN Lawyers &amp; Notary">
      <div class="firm-name">
        <span class="firm-name__main">KD LORN</span>
        <span class="firm-name__sub">Lawyers &amp; Notary</span>
      </div>

      <div class="rule-thin rule-thin--upper"></div>

      <div class="name-band">
        <h1 class="holder-name">Clara Bexley</h1>
        <div class="name-divider"></div>
        <p class="holder-credentials">Solicitor · Notary Public (Qld &amp; Vic) · Migration Agent<br>LLB, LLM, Grad Dip in LP, Grad Dip in NP · RMA 0853162</p>
      </div>

      <div class="rule-thin rule-thin--lower"></div>

      <p class="slogan">Every Matter Handled with Steady Care</p>

      <div class="contact-details">
        <ul class="contact-column">
          <li><span class="contact-label">Office:</span> 24/6 Tolvern Road Marleigh QLD 4287 Australia</li>
          <li><span class="contact-label">Postal:</span> P O Box 61 Marleigh QLD 4287 Australia</li>
          <li><span class="contact-label">Tel:</span> 1300 274 563 &nbsp; <span class="contact-label">Fax:</span> 1300 274 569</li>
          <li><span class="contact-label">Intl Tel:</span> +617 3956 2740 &nbsp; <span class="contact-label">Intl Fax:</span> +617 3871 6025</li>
        </ul>
        <ul class="contact-column">
          <li>&nbsp;</li>
          <li>clara.bexley@kdlornlegal.example</li>
          <li><span class="contact-label">Web:</span> www.kdlornlegal.example</li>
          <li>&nbsp;</li>
        </ul>
      </div>
    </section>
  </main>
</body>
</html>
```